~~ Night Club Website ~~

We would like to redo our website for Halo Velvet Room (http://www.halovelvetroom-example.com).

Halo Velvet Room is Edmonton's #1 electronic dance music night club.

We have DJs that fly in from around the world to play at our club and want to be able to properly showcase our upcoming shows and events to increase sales.
Updates

I have now guaranteed the project.  Let's see some brilliant designs!

Target Market(s)

Electronic Dance Music Lovers; College / University Students; Young Professionals

Industry/Entity Type

Electronic

Requirements
Must have
• The site must have the following sections:

1. Home Page
- Rotating Banner where we can put upcoming events
- Chirper, Facepage, ClipTube, FourSquare buttons
- Our Chirper feed to automatically post
- Facepage integration with 'Like' and Comments for upcoming shows
- An email signup section for contests and giveaways that auto-updates the email list in MailChimp
- Streaming music from 9 Pulse Radio

2. Photos
- This needs to integrate right into our Facepage Albums

3. Weekly Lineup

4. Events
- People need to be able to buy tickets right online via PayPal

5. Bookings
- People need to be able to pick a party package and pay right online via PayPal

6. Contact Us

```html
<!DOCTYPE html>
<html lang="en">
<head>
<meta charset="utf-8">
<title>Halo Velvet Room</title>
<link href="https://fonts.googleapis.com/css2?family=PT+Sans:wght@400;700&display=swap" rel="stylesheet">
<style>
:root{
  --black:#0a0a0a;
  --bar:#1c1c1c;
  --orange:#f2a20a;
  --orange-dark:#d27e00;
  --grey-body:#e9e9e9;
  --grey-foot:#d9d9d9;
  --grey-box:#c9c9c9;
  --text:#777;
  --heading:#3a3a3a;
  --white:#fff;
}
*{box-sizing:border-box;margin:0;padding:0}
html,body{width:1089px;height:1200px;overflow:hidden;background:var(--grey-body)}
body{font-family:"PT Sans",sans-serif;position:relative;color:var(--text)}
.abs{position:absolute}
.hero-art{left:0;top:0;width:1089px;height:449px;
  background:radial-gradient(circle at 30% 40%,#e8461a 0,#b0241a 18%,transparent 38%),
  radial-gradient(circle at 12% 25%,#1f8fb0 0,transparent 30%),
  radial-gradient(circle at 55% 20%,#3a2a88 0,transparent 28%),
  radial-gradient(circle at 75% 10%,#2c3f8a 0,transparent 25%),#050505}
.crowd{left:0;top:300px;width:640px;height:149px;background:linear-gradient(180deg,transparent,#000 60%)}
.topbar{left:0;top:0;width:1089px;height:65px;background:rgba(0,0,0,.85)}
.nav{left:262px;top:65px;width:827px;height:35px;background:linear-gradient(#3a3a3a,#141414);border-top:1px solid #555;border-bottom:1px solid #555}
.nav-left{left:0;top:65px;width:102px;height:35px;background:linear-gradient(#3a3a3a,#141414);border-top:1px solid #555;border-bottom:1px solid #555}
.nav a{position:absolute;top:8px;color:var(--white);font-size:13px;text-decoration:none;transform:translateX(-50%)}
.logo{left:107px;top:11px;width:150px;height:150px;border-radius:50%;background:radial-gradient(#1a1a1a,#000);border:3px solid #444;box-shadow:0 0 10px #000;display:flex;align-items:center;justify-content:center;flex-direction:column}
.logo .mark{width:16px;height:16px;background:var(--white);margin-bottom:8px}
.logo span{color:var(--white);font-size:17px;font-weight:700;text-align:center;line-height:1.1}
.player{left:344px;top:14px;width:344px;height:36px;border-radius:5px;background:#151515;border:1px solid #333;color:var(--white);font-size:10px}
.player .time{position:absolute;left:86px;top:11px}
.player .track{position:absolute;left:160px;top:16px;width:118px;height:4px;background:#444;border-radius:2px}
.player .fill{width:50px;height:4px;background:var(--orange);border-radius:2px}
.player .knob{position:absolute;left:46px;top:-4px;width:12px;height:12px;border-radius:50%;background:#ddd}
.social{top:18px;color:var(--white);font-size:12px;font-weight:700}
.cart{left:871px;top:16px;color:var(--white);font-size:11px;line-height:1.2}
.cart .bag{position:absolute;left:0;top:4px;width:19px;height:20px;background:var(--orange)}
.cart p{margin-left:32px}
.hero-h1{left:524px;top:184px;color:var(--white);font-size:53px;font-weight:700;line-height:1}
.hero-h2{left:524px;top:230px;color:var(--white);font-size:33px;line-height:1}
.hero-p{left:527px;top:270px;width:350px;color:var(--white);font-size:11px;line-height:13px}
.dots{left:891px;top:385px;display:flex;gap:5px}
.dots i{width:14px;height:14px;border-radius:50%;background:#555;border:1px solid #222}
.dots i.on{background:var(--white)}
.features{left:113px;top:412px;width:862px;height:113px;background:linear-gradient(#2b2b2b,#000 45%);border-radius:8px 8px 50% 50%/8px 8px 22px 22px;border:1px solid #444;box-shadow:0 8px 14px rgba(0,0,0,.35)}
.feature{position:absolute;top:0;height:112px;color:var(--white)}
.feature h3{font-size:18px;font-weight:700;margin-top:8px}
.feature p{font-size:11px;line-height:13px;margin-top:6px}
.divider{position:absolute;top:0;width:1px;height:112px;background:#444}
.btn{display:inline-block;background:linear-gradient(var(--orange),var(--orange-dark));color:#2a1600;font-weight:700;font-size:13px;padding:3px 11px;border-radius:2px;border:1px solid #b86b00}
.btn.small{font-size:11px;font-weight:400;padding:3px 7px}
.email{width:210px;height:19px;background:var(--white);border:1px solid #999;font-size:9px;color:#888;padding:3px 9px;margin-top:10px}
h2.sec{color:var(--heading);font-size:17px;font-weight:700}
.col p{font-size:11px;line-height:13px}
.thumb{border:3px solid var(--white);box-shadow:0 1px 3px rgba(0,0,0,.35)}
.crowd-faint{left:70px;top:815px;width:950px;height:98px;background:linear-gradient(transparent,#d4d4d4);opacity:.8}
.footer-band{left:0;top:913px;width:1089px;height:260px;background:var(--grey-foot)}
.map{left:125px;top:967px;width:265px;height:187px;background:linear-gradient(#efefef,#e2e2e2);border:1px solid #bbb}
.bubble{left:425px;top:984px;width:229px;height:169px;background:var(--grey-box);border-radius:12px;padding:8px 17px}
.bubble p,.fb p{font-size:11px;line-height:13px;color:#555}
.bubble small,.fb small{display:block;font-size:11px;color:#888;margin-bottom:6px}
.fb{left:693px;top:955px;width:282px;height:198px;background:var(--grey-box);border:1px solid #bbb}
.fb .item{position:absolute;left:12px;display:flex;gap:13px}
.fb .pic{width:52px;height:52px;border:2px solid var(--white);flex:none}
.bottom{left:0;top:1173px;width:1089px;height:27px;background:#3a3a3a;color:var(--white);font-size:11px;text-align:right;padding:6px 115px 0 0}
</style>
</head>
<body>
<div class="abs hero-art" role="img" aria-label="Club night photo with colourful bokeh lights"></div>
<div class="abs crowd" role="img" aria-label="Silhouettes of dancing crowd"></div>
<div class="abs topbar"></div>
<div class="abs nav-left"></div>
<nav class="abs nav">
  <a style="left:48px">Home</a><a style="left:145px">Photos</a><a style="left:267px">Weekly Specials</a>
  <a style="left:388px">Events</a><a style="left:495px">Bookings</a><a style="left:613px">Contact Us</a>
</nav>
<div class="abs logo"><div class="mark"></div><span>HALO VELVET<br>ROOM</span></div>

<div class="abs player">
  <svg class="abs" style="left:12px;top:11px" width="70" height="14" fill="#fff">
    <rect x="0" y="1" width="3" height="12"/><rect x="6" y="1" width="3" height="12"/>
    <rect x="30" y="1" width="2" height="12"/><polygon points="42,1 42,13 33,7"/>
    <polygon points="54,1 54,13 63,7"/><rect x="64" y="1" width="2" height="12"/>
  </svg>
  <span class="time">01:18 / 03:39</span>
  <div class="track"><div class="fill"></div><div class="knob"></div></div>
  <svg class="abs" style="left:290px;top:11px" width="46" height="14" fill="#fff">
    <path d="M0 3h5l6 8h4M0 11h5l6-8h4" stroke="#fff" stroke-width="1.5" fill="none"/>
    <polygon points="24,5 28,5 32,1 32,13 28,9 24,9"/>
    <rect x="36" y="2" width="6" height="2" fill="#f2a20a"/><rect x="36" y="6" width="6" height="2" fill="#f2a20a"/><rect x="36" y="10" width="6" height="2" fill="#f2a20a"/>
  </svg>
</div>

<span class="abs social" style="left:718px">Chirper</span>
<span class="abs social" style="left:765px">ClipTube</span>
<span class="abs social" style="left:814px;top:32px">Facepage</span>

<div class="abs cart"><div class="bag"></div><p><b>Your cart empty</b><br>0 items</p></div>

<h1 class="abs hero-h1">Come for a Drink</h1>
<div class="abs hero-h2">Stay for the experience</div>
<p class="abs hero-p">Our collection of well known Resident DJ’s will be spinning your favorite tracks and guiding your musical entertainment in House, Dirty Electro, and funky Mashups</p>
<div class="abs dots"><i></i><i></i><i></i><i class="on"></i></div>

<section class="abs features">
  <div class="feature" style="left:85px;width:200px;text-align:right">
    <h3>Weekly Specials</h3>
    <p>Lorem ipsum dolor sit amet, consectetuer adipiscing elit, sed diam nonummy ......</p>
    <span class="btn" style="margin-top:7px">Check Now</span>
  </div>
  <div class="divider" style="left:293px"></div>
  <div class="feature" style="left:315px;width:245px">
    <h3>Book your tickets now</h3>
    <p>Lorem ipsum dolor sit amet, consectetuer adipiscing elit, sed diam nonummy ......</p>
    <span class="btn" style="margin-top:7px">Book Now</span>
  </div>
  <div class="divider" style="left:557px"></div>
  <div class="feature" style="left:579px;width:240px">
    <h3>Newsletter Signup</h3>
    <div class="email">Email Address</div>
    <span class="btn" style="margin-top:11px">Submit</span>
  </div>
</section>

<div class="abs crowd-faint" role="img" aria-label="Faint silhouette of dancing crowd"></div>

<section class="abs col" style="left:123px;top:548px;width:255px">
  <h2 class="sec">Welcome to Halo Velvet Room</h2>
  <p style="color:#333;margin-top:2px">Marlow Avenue’s Premium Bottle Service Lounge</p>
  <p style="margin-top:13px">Enjoy friendly service from when you first arrive at the door and throughout your night from our bartenders and servers.</p>
  <p style="margin-top:13px">Our collection of well known Resident DJ’s will be spinning your favorite tracks and guiding your musical entertainment in House, Dirty Electro, and funky Mashups</p>
  <p style="margin-top:13px">Dress to impress and relax with friends in one of our VIP booths and receive personalized bottle service - Please call ahead to make reservations</p>
  <span class="btn small" style="margin-top:14px">Read More</span>
</section>
<div class="abs" style="left:405px;top:548px;width:1px;height:210px;background:#ccc"></div>

<h2 class="abs sec" style="left:424px;top:548px">Latest Events</h2>
<div class="abs thumb" style="left:426px;top:579px;width:94px;height:94px;background:linear-gradient(#2a1a8a,#8a7ee0)" role="img" aria-label="Event photo of a stage and crowd"></div>
<div class="abs col" style="left:528px;top:578px;width:135px">
  <p style="color:#333;font-size:13px;font-weight:700">Event Name</p>
  <p style="margin-top:3px">Lorem ipsum dolor sit amet, consectetuer adipiscing elit, sed diam nonummy ......</p>
  <span class="btn small" style="margin-top:6px">Book Now</span>
</div>
<div class="abs thumb" style="left:426px;top:698px;width:94px;height:94px;background:linear-gradient(135deg,#3fb0d8,#1a2a4a)" role="img" aria-label="Event photo of DJ mixing decks"></div>
<div class="abs col" style="left:528px;top:697px;width:135px">
  <p style="color:#333;font-size:13px;font-weight:700">Event Name</p>
  <p style="margin-top:3px">Lorem ipsum dolor sit amet, consectetuer adipiscing elit, sed diam nonummy ......</p>
  <span class="btn small" style="margin-top:6px">Book Now</span>
</div>
<div class="abs" style="left:670px;top:548px;width:1px;height:110px;background:#ccc"></div>

<h2 class="abs sec" style="left:693px;top:548px">Event Photos</h2>
<div class="abs thumb" style="left:693px;top:583px;width:79px;height:79px;background:linear-gradient(#3a1a4a,#a05a7a)" role="img" aria-label="Crowd photo"></div>
<div class="abs thumb" style="left:794px;top:583px;width:79px;height:79px;background:linear-gradient(#c0307a,#e8a0c0)" role="img" aria-label="DJ photo"></div>
<div class="abs thumb" style="left:894px;top:583px;width:79px;height:79px;background:linear-gradient(#3a0a0a,#c04020)" role="img" aria-label="Stage performers photo"></div>
<div class="abs thumb" style="left:693px;top:684px;width:79px;height:79px;background:linear-gradient(#1a1a1a,#6a5a5a)" role="img" aria-label="Dancing crowd photo"></div>
<div class="abs thumb" style="left:794px;top:684px;width:79px;height:79px;background:linear-gradient(#6a6ae0,#1a1a6a)" role="img" aria-label="Arena light show photo"></div>
<div class="abs thumb" style="left:894px;top:684px;width:79px;height:79px;background:linear-gradient(135deg,#1a90e0,#d0e8f8)" role="img" aria-label="Performer under lights photo"></div>

<div class="abs footer-band"></div>
<h2 class="abs sec" style="left:127px;top:939px">Contact Us</h2>
<div class="abs map" role="img" aria-label="Street map showing the club location"></div>

<div class="abs" style="left:432px;top:930px;font-size:28px;font-weight:700;color:#9a9a9a">Chirper</div>
<div class="abs" style="left:436px;top:964px;font-size:13px;font-weight:700;color:#333">Find Updates</div>
<svg class="abs" style="left:572px;top:970px" width="30" height="16"><polygon points="0,16 14,0 28,16" fill="#c9c9c9"/></svg>
<div class="abs bubble">
  <p>Lorem ipsum dolor sit amet, consectetuer adipiscing elit, sed diam nonummy ......</p><small>less than a min ago</small>
  <p>Lorem ipsum dolor sit amet, consectetuer adipiscing elit, sed diam nonummy ......</p><small>less than a min ago</small>
  <p>Lorem ipsum dolor sit amet, consectetuer adipiscing elit, sed diam nonummy ......</p><small>less than a min ago</small>
</div>

<h2 class="abs sec" style="left:695px;top:929px">Find us on Facepage</h2>
<div class="abs fb">
  <div class="item" style="top:11px"><div class="pic" style="background:linear-gradient(#5a2a4a,#d09ab0)" role="img" aria-label="Fan photo"></div><div><p>Lorem ipsum dolor sit amet, consectetuer adipiscing elit, sed diam nonummy ......</p><small>less than a min ago</small></div></div>
  <div class="item" style="top:72px"><div class="pic" style="background:linear-gradient(#1a5a7a,#3a2a2a)" role="img" aria-label="Fan photo"></div><div><p>Lorem ipsum dolor sit amet, consectetuer adipiscing elit, sed diam nonummy ......</p><small>less than a min ago</small></div></div>
  <div class="item" style="top:133px"><div class="pic" style="background:linear-gradient(#e04080,#4aa0c0)" role="img" aria-label="Fan photo"></div><div><p>Lorem ipsum dolor sit amet, consectetuer adipiscing elit, sed diam nonummy ......</p><small>less than a min ago</small></div></div>
</div>

<footer class="abs bottom">Copyrights@halovelvetroom-example.com, All rights reserved</footer>
</body>
</html>
```